Recycling Depot Business Card Design

We need a double sided business card for our recycling depot business. Please include name, position, address, phone, cell, fax, email and website address. Business card should match the colour scheme of our logo and look environmental but modern. I've attached a few business cards from Sketch Harbor that I like.

Industry/Entity Type

Recycling

Contact Information for Business Card

Please include name, position, address, phone, cell, fax, email and website address.

Font styles to use
Sans Serif

Requirements
Must have
• Our Logo, Colour Scheme that matches our logo. Use of Colour Gradients and a custom look.

```html
<!DOCTYPE html>
<html lang="en">
<head>
<meta charset="utf-8">
<title>Greenloop Business Card</title>
<link rel="stylesheet" href="https://fonts.googleapis.com/css2?family=Roboto+Condensed:wght@400;700&display=swap">
<style>
  :root {
    --page-bg: #d9d4cc;
    --panel-dark: #1b211c;
    --frost-light: #eeeae4;
    --frost-shade: #d6d1c9;
    --green-bright: #4f9a2e;
    --green-deep: #1f4d17;
    --green-logo: #2f6b1e;
    --text-light: #e2e4e0;
  }
  * { margin: 0; padding: 0; box-sizing: border-box; }
  html, body { width: 1200px; height: 969px; overflow: hidden; }
  body {
    background: var(--page-bg);
    font-family: "Roboto Condensed", sans-serif;
    position: relative;
  }
  .card {
    position: absolute;
    left: 100px; top: 200px;
    width: 1000px; height: 570px;
    border-radius: 26px;
    overflow: hidden;
    background: linear-gradient(135deg, var(--frost-light), var(--frost-shade));
    box-shadow: 0 10px 30px rgba(0,0,0,.18);
  }
  .card-shape { position: absolute; inset: 0; }
  .contact-block {
    position: absolute;
    left: 78px; top: 118px;
    color: var(--text-light);
  }
  .holder-name {
    font-size: 31px; font-weight: 700;
    color: var(--green-bright);
    line-height: 1;
  }
  .holder-title { font-size: 22px; margin-top: 6px; }
  .address { font-size: 22px; line-height: 30px; margin-top: 22px; }
  .contact-list { list-style: none; margin-top: 22px; }
  .contact-list li {
    font-size: 22px; line-height: 29px;
    display: flex; align-items: center; gap: 12px;
  }
  .contact-list svg { width: 20px; height: 20px; flex: none; }
  .brand {
    position: absolute;
    left: 530px; top: 250px;
    display: flex; align-items: center; gap: 18px;
  }
  .brand-dot {
    width: 60px; height: 60px; border-radius: 50%;
    background: var(--green-logo);
  }
  .brand-name {
    font-size: 66px; font-weight: 700;
    color: var(--green-logo);
    line-height: 1;
  }
</style>
</head>
<body>
  <div class="card">
    <svg class="card-shape" viewBox="0 0 1000 570" width="1000" height="570">
      <defs>
        <radialGradient id="panelGlow" cx="0.45" cy="0.4" r="0.8">
          <stop offset="0" stop-color="#3a433b"/>
          <stop offset="1" stop-color="#161b17"/>
        </radialGradient>
      </defs>
      <path d="M0 0 H432 C378 60 360 180 400 285 C440 370 500 440 414 570 H0 Z" fill="url(#panelGlow)"/>
    </svg>

    <div class="contact-block">
      <div class="holder-name">Daniel Brooks</div>
      <div class="holder-title">President</div>
      <div class="address">4213 Willow Bend Road<br>Fairbanks, Alaska 45812</div>
      <ul class="contact-list">
        <li><svg viewBox="0 0 20 20"><path d="M4 2 L8 2 L9 6 L7 8 C8 11 9 12 12 13 L14 11 L18 12 L18 16 C18 17 17 18 16 18 C8 18 2 12 2 4 C2 3 3 2 4 2 Z" fill="var(--green-bright)"/></svg>555-214-7730</li>
        <li><svg viewBox="0 0 20 20"><rect x="5" y="1" width="10" height="18" rx="2" fill="none" stroke="var(--green-bright)" stroke-width="2"/><circle cx="10" cy="15.5" r="1.2" fill="var(--green-bright)"/></svg>555-618-2049</li>
        <li><svg viewBox="0 0 20 20"><rect x="5" y="3" width="10" height="5" fill="var(--green-bright)"/><rect x="2" y="8" width="16" height="7" rx="1" fill="var(--green-bright)"/><rect x="5" y="13" width="10" height="5" fill="var(--green-deep)"/></svg>555-390-4621</li>
        <li><svg viewBox="0 0 20 20"><rect x="2" y="5" width="16" height="11" fill="var(--green-bright)"/><path d="M2 5 L10 11 L18 5" fill="none" stroke="var(--panel-dark)" stroke-width="1.5"/></svg>info@greenloopdepot.com</li>
        <li><svg viewBox="0 0 20 20"><circle cx="10" cy="10" r="8" fill="var(--green-bright)"/><path d="M2 10 H18 M10 2 C6 6 6 14 10 18 C14 14 14 6 10 2" fill="none" stroke="var(--panel-dark)" stroke-width="1.2"/></svg>www.greenloopdepot.com</li>
      </ul>
    </div>

    <div class="brand">
      <div class="brand-dot"></div>
      <div class="brand-name">Greenloop</div>
    </div>
  </div>
</body>
</html>
```